Lanternfield Disability - Social Security Disability Attorneys

Our company is expanding to attract clients nationwide for our social security disability practice. We have a logo, but I am looking for a creative and elegant letterhead that projects an image of being technologically advanced but still professional enough for the legal field. I am looking for the "wow factor" combined with this is still professional enough for a law practice.

Requesting letterhead and business card design
Updates

Had to update and change the logo. The previous logo had a typo. Please send updates with the new logo for consideration. The letterhead and business cards should be professional enough to be used for a law firm. Thanks.

Industry/Entity Type

Law Practice, Law Firm, Healthcare Industry, Government

Colors

Designer to choose colors to be used in the design.

Requirements
Nice to have
• **Please create a vertical design for the business card**

```html
<!DOCTYPE html>
<html lang="en">
<head>
<meta charset="utf-8">
<title>Lanternfield Disability – Stationery</title>
<link href="https://fonts.googleapis.com/css2?family=Arimo:wght@400;700&display=swap" rel="stylesheet">
<style>
  :root{
    --bg:#d7dedf;
    --paper:#f4f4f4;
    --ink:#1e1e1e;
    --muted:#555;
    --blue:#1565d8;
    --sky:#18b4ea;
    --orange:#f47b20;
    --rule:#d6d6d6;
    --card-dark:#141414;
  }
  *{box-sizing:border-box;margin:0;padding:0}
  html,body{width:750px;height:1200px;overflow:hidden;background:var(--bg);font-family:"Arimo",Arial,sans-serif;color:var(--ink)}
  .canvas{position:relative;width:750px;height:1200px}

  /* Letterhead */
  .letterhead{position:absolute;left:155px;top:30px;width:440px;height:570px;background:var(--paper);box-shadow:0 4px 14px rgba(0,0,0,.18);overflow:hidden}
  .lh-header{position:absolute;left:32px;right:32px;top:30px}
  .lh-name{position:absolute;left:0;top:42px;font-size:17px;color:var(--blue);letter-spacing:.3px}
  .lh-contact{position:absolute;right:0;top:0;text-align:right;font-size:6.3px;line-height:8.4px;color:var(--ink)}
  .lh-contact .gap{height:8px}
  .lh-contact .row{display:flex;justify-content:flex-end;align-items:center;gap:3px}
  .lh-contact svg{width:6px;height:6px}
  .lh-rules{position:absolute;left:0;right:0;top:67px}
  .lh-rules .o{height:1.5px;background:var(--orange)}
  .lh-rules .b{height:1.5px;background:var(--blue);margin-top:1px}
  .lh-body{position:absolute;left:32px;right:52px;top:150px;font-size:6.4px;line-height:8.2px}
  .lh-body p{margin-bottom:8px}
  .lh-body .to strong{font-weight:700}
  .lh-sign{font-size:13px;font-style:italic;color:var(--ink);margin-top:6px}
  .lh-footer{position:absolute;left:0;right:0;bottom:14px}
  .lh-footer .o{height:3px;background:var(--orange)}
  .lh-footer .b{height:18px;margin-top:2px;background:linear-gradient(90deg,var(--blue),var(--sky))}

  /* Business cards */
  .card{position:absolute;left:165px;width:420px;height:240px;box-shadow:0 4px 14px rgba(0,0,0,.25);overflow:hidden}
  .card-back{top:640px;background:var(--card-dark)}
  .card-back .brand{position:absolute;left:0;right:0;top:108px;text-align:center;font-size:17px;color:#f2f2f2;letter-spacing:.5px}
  .card-front{top:900px;background:#fff}
  .cf-brand{position:absolute;right:24px;top:34px;font-size:20px;color:var(--blue);letter-spacing:.3px}
  .cf-rule{position:absolute;left:150px;right:24px;top:76px;height:1px;background:var(--rule)}
  .cf-person{position:absolute;left:28px;top:112px}
  .cf-person .name{font-size:21px;font-weight:700;color:var(--blue)}
  .cf-person .role{font-size:12px;color:var(--muted);margin-top:2px}
  .cf-address{position:absolute;left:28px;top:166px;display:flex;gap:10px;font-size:12px;line-height:16px;color:var(--ink)}
  .cf-address svg{width:11px;height:14px;margin-top:2px}
  .cf-contact{position:absolute;right:24px;top:104px;font-size:11.5px;line-height:16px;text-align:right;color:var(--ink)}
  .cf-contact .row{display:flex;justify-content:flex-end;align-items:center;gap:9px}
  .cf-contact svg{width:10px;height:10px}
  .cf-band{position:absolute;left:0;right:0;bottom:0;height:9px;background:var(--orange)}
</style>
</head>
<body>
<div class="canvas">

  <section class="letterhead">
    <header class="lh-header">
      <div class="lh-name">LANTERNFIELD DISABILITY</div>
      <div class="lh-contact">
        <div>418 Harbor Ridge Rd Suite 120</div>
        <div>Cedar Bay, Texas 77504</div>
        <div class="gap"></div>
        <div class="row">555-014-2870
          <svg viewBox="0 0 10 10"><path d="M2 1l2 2-1 1.2c.6 1.2 1.6 2.2 2.8 2.8L7 6l2 2-1.2 1.2C4.5 9 1 5.5.8 2.2z" fill="var(--blue)"/></svg></div>
        <div class="row">support@lanternfielddisability.com
          <svg viewBox="0 0 10 10"><rect x="1" y="2" width="8" height="6" fill="var(--blue)"/><path d="M1 2l4 3 4-3" stroke="#fff" fill="none" stroke-width=".8"/></svg></div>
        <div class="row">www.lanternfielddisability.com
          <svg viewBox="0 0 10 10"><circle cx="5" cy="5" r="4" fill="var(--blue)"/><path d="M1 5h8M5 1v8" stroke="#fff" stroke-width=".6"/></svg></div>
      </div>
      <div class="lh-rules"><div class="o"></div><div class="b"></div></div>
    </header>

    <main class="lh-body">
      <p class="to"><strong>Someone Some body</strong><br>1001 Long Street<br>New York City, USA</p>
      <p>Dear Someone Somebody,</p>
      <p>Lorem ipsum dolor sit amet, consectetur adipiscing elit. Nunc ac magna tellus, vitae hendrerit mauris. Donec consectetur rhoncus nunc, vitae imperdiet leo viverra ut. Pellentesque fermentum mi ac erat ultricies faucibus. Nam gravida nibh non lacus fermentum porta. Nulla non placerat turpis. Maecenas quis metus sem. Nullam nisi lacus, egestas sit amet porttitor nec, consectetur eget neque. Vivamus ultricies ultrices turpis, vel porttitor odio sagittis a. Pellentesque accumsan, lacus at suscipit rutrum, erat tortor imperdiet purus, semper congue augue turpis eget est. Curabitur blandit, orci ut accumsan fermentum, lorem metus auctor nisl, eget sodales elit libero id mi. Nullam sed lorem augue, ut tristique dui.</p>
      <p>Pellentesque vehicula pulvinar libero et ultricies. In hac habitasse platea dictumst. Phasellus eget quam lectus, pellentesque condimentum nulla. Morbi consequat euismod purus ut auctor. Cras convallis eleifend vehicula. Sed facilisis egestas accumsan. Duis in blandit velit. Curabitur diam eros, volutpat et iaculis ut, suscipit at est.</p>
      <p>Aenean id diam enim. Donec vitae arcu quam. Nunc mollis feugiat pretium. Praesent vel ligula felis. Ut sed velit nibh. Suspendisse faucibus convallis scelerisque. Sed sodales, nisi vitae placerat eleifend, lorem nulla iaculis leo, in lacinia metus sem quis purus. Ut non felis felis, pharetra fermentum purus. Suspendisse potenti. Nunc non faucibus ligula. Phasellus ipsum velit, laoreet ut scelerisque vel, commodo at felis. Donec malesuada malesuada aliquam. Aliquam justo elit, dapibus vitae hendrerit hendrerit, commodo sed ipsum. Donec ultricies mi non felis sollicitudin et elementum augue adipiscing. Integer quam purus, venenatis in ornare ac, sagittis quis purus.</p>
      <p>Youre Sincerely,</p>
      <div class="lh-sign">Signature</div>
    </main>

    <footer class="lh-footer"><div class="o"></div><div class="b"></div></footer>
  </section>

  <section class="card card-back">
    <div class="brand">LANTERNFIELD DISABILITY</div>
  </section>

  <section class="card card-front">
    <div class="cf-brand">LANTERNFIELD DISABILITY</div>
    <div class="cf-rule"></div>
    <div class="cf-person">
      <div class="name">Marisol Keane</div>
      <div class="role">Manager</div>
    </div>
    <div class="cf-address">
      <svg viewBox="0 0 10 14"><path d="M5 0a5 5 0 0 0-5 5c0 3.5 5 9 5 9s5-5.5 5-9a5 5 0 0 0-5-5z" fill="var(--orange)"/><circle cx="5" cy="5" r="2" fill="#fff"/></svg>
      <div>418 Harbor Ridge Rd Suite 120,<br>Cedar Bay, Texas 77504</div>
    </div>
    <div class="cf-contact">
      <div class="row">555 201 7730
        <svg viewBox="0 0 10 10"><path d="M2 1l2 2-1 1.2c.6 1.2 1.6 2.2 2.8 2.8L7 6l2 2-1.2 1.2C4.5 9 1 5.5.8 2.2z" fill="var(--orange)"/></svg></div>
      <div class="row">555 201 7741
        <svg viewBox="0 0 10 10"><rect x="2.5" y=".5" width="5" height="9" rx="1" fill="none" stroke="var(--orange)" stroke-width="1.2"/></svg></div>
      <div class="row">info@lanternfielddisability.com
        <svg viewBox="0 0 10 10"><rect x="1" y="2" width="8" height="6" fill="var(--orange)"/><path d="M1 2l4 3 4-3" stroke="#fff" fill="none" stroke-width=".8"/></svg></div>
      <div class="row">www.lanternfielddisability.com
        <svg viewBox="0 0 10 10"><circle cx="5" cy="5" r="4" fill="var(--orange)"/><path d="M1 5h8M5 1v8" stroke="#fff" stroke-width=".6"/></svg></div>
    </div>
    <div class="cf-band"></div>
  </section>

</div>
</body>
</html>
```